Real Estate Agent need a business card

I am a real estate agent in Vancouver, BC Canada. I recently used PixelHarbor to develop a logo of my own. I would like to have my logo in the business card, as well my realty office logo also must be displayed along with its address. I also would like to have my headshot photo displayed in the business card on both sides.

Industry/Entity Type

Real Estate Agent

Contact Information for Business Card

My office address:
Bramwell Peak Realty
2271 Lindqvist St.
Vancouver, BC V5K 2P8

My contact information:
Cell: 604-555-0148
Office: 604-555-0192
Fax: 604-555-0193

My website : www.danielmorvik.example
My email: email@danielmorvik.example

My slogan: Simply I do. Far and Above.

Requirements
Must have
• Front side(all in colour): My photo, My own logo, My office logo, My cell number, My website address and email, My slogan.
• Back side(could be black & white/ plz refer to the file name "preview"): My photo, My own logo, my office logo, my office address, my contact information.
• * Please read this: Since my logo has my name in it, there is no need to put my name in the card separately. As well, my office logo MUST BE displayed on both sides(you can reduce the size of office logo). But the office address can be displayed only one side, front or back. I would prefer to have my cell number only to be displayed prominently on the front side. So all the numbers should be displayed on the backside instead. Remember that I am trying to promote myself so the most important thing I consider from the front side of the card is my cell number, my website, and my email, not the office. The only thing I require by industry regulation from the front side is my office logo. Hope this helps.
Nice to have
• Colour on the front side and the black and white on the back side

```html
<!DOCTYPE html>
<html lang="en">
<head>
<meta charset="utf-8">
<title>Daniel Morvik – Business Card</title>
<link rel="stylesheet" href="https://fonts.googleapis.com/css2?family=Exo+2:wght@400;500;700&display=swap">
<style>
  :root {
    --bg: #e9e6e0;
    --card: #ffffff;
    --card-shade: #eeeeee;
    --green: #7dc242;
    --charcoal: #4a4b4d;
    --ink: #4f5052;
    --muted: #8a8b8d;
    --white: #ffffff;
    --photo-light: #d9dadb;
    --photo-dark: #9c9ea1;
  }
  * { box-sizing: border-box; margin: 0; padding: 0; }
  html, body {
    width: 1056px; height: 1200px; overflow: hidden;
    background: var(--bg);
    font-family: "Exo 2", sans-serif;
  }
  .card {
    position: absolute; top: 232px;
    width: 420px; height: 735px;
    background: radial-gradient(circle at 60% 30%, var(--card) 0%, var(--card) 45%, var(--card-shade) 100%);
    box-shadow: 0 14px 30px rgba(0,0,0,.18);
    overflow: hidden;
  }
  .card--front { left: 84px; }
  .card--back { left: 552px; }

  /* agent brand */
  .brand { position: absolute; display: flex; align-items: center; gap: 14px; }
  .brand__mark { width: 40px; height: 40px; background: var(--green); flex: none; }
  .brand__name { font-weight: 700; color: var(--charcoal); font-size: 28px; letter-spacing: .5px; line-height: 1; }
  .brand__tagline { font-weight: 500; color: var(--green); font-size: 12px; letter-spacing: 3px; margin-top: 6px; }
  .card--front .brand { top: 64px; left: 56px; }
  .card--back .brand { top: 64px; left: 56px; }

  /* headshot placeholder */
  .headshot {
    position: absolute; left: 56px; top: 160px;
    width: 124px; height: 156px; border-radius: 6px;
    background: linear-gradient(160deg, var(--photo-light), var(--photo-dark));
  }

  /* office mark */
  .office { position: absolute; display: flex; align-items: center; gap: 10px; }
  .office__mark { width: 14px; height: 14px; background: var(--charcoal); flex: none; }
  .office__name { font-size: 13px; font-weight: 700; color: var(--charcoal); letter-spacing: 1px; }

  /* front */
  .cell { position: absolute; left: 204px; top: 196px; }
  .cell__label { font-size: 13px; font-weight: 500; color: var(--green); letter-spacing: 3px; }
  .cell__number { font-size: 26px; font-weight: 700; color: var(--charcoal); margin-top: 4px; }
  .card--front .office { left: 56px; top: 448px; }

  .contacts { position: absolute; left: 56px; list-style: none; }
  .contacts li { display: flex; align-items: center; gap: 12px; height: 32px; color: var(--ink); font-size: 15px; }
  .contacts svg { width: 20px; height: 20px; flex: none; }
  .card--front .contacts { top: 350px; }
  .card--back .contacts { top: 350px; }
  .contacts__label { width: 52px; color: var(--muted); font-size: 13px; letter-spacing: 1px; }

  /* back */
  .card--back .office { left: 200px; top: 172px; }
  .address { position: absolute; left: 200px; top: 204px; color: var(--ink); font-size: 15px; line-height: 1.5; }

  .swoosh { position: absolute; left: 0; bottom: 0; width: 420px; height: 230px; }
  .band-text {
    position: absolute; left: 34px; bottom: 46px;
    color: var(--white); letter-spacing: 2px;
  }
  .slogan { font-size: 19px; font-weight: 500; line-height: 1.35; }
  .website { font-size: 16px; letter-spacing: 1px; }
</style>
</head>
<body>

<section class="card card--front">
  <div class="brand">
    <span class="brand__mark"></span>
    <div>
      <div class="brand__name">DANIEL MORVIK</div>
      <div class="brand__tagline">REAL ESTATE AGENT</div>
    </div>
  </div>

  <div class="headshot" role="img" aria-label="Headshot photo of the agent"></div>

  <div class="cell">
    <div class="cell__label">CELL</div>
    <div class="cell__number">604-555-0148</div>
  </div>

  <ul class="contacts">
    <li>
      <svg viewBox="0 0 20 20"><rect width="20" height="20" rx="3" fill="var(--green)"/><rect x="4" y="6" width="12" height="8.5" fill="var(--white)"/><path d="M4 6l6 5 6-5" fill="none" stroke="var(--green)" stroke-width="1.2"/></svg>
      email@danielmorvik.example
    </li>
    <li>
      <svg viewBox="0 0 20 20"><rect width="20" height="20" rx="3" fill="var(--green)"/><circle cx="10" cy="10" r="5.5" fill="none" stroke="var(--white)" stroke-width="1.3"/><path d="M4.5 10h11M10 4.5c-2.5 3-2.5 8 0 11M10 4.5c2.5 3 2.5 8 0 11" fill="none" stroke="var(--white)" stroke-width="1.1"/></svg>
      www.danielmorvik.example
    </li>
  </ul>

  <div class="office">
    <span class="office__mark"></span>
    <span class="office__name">BRAMWELL PEAK REALTY</span>
  </div>

  <svg class="swoosh" viewBox="0 0 420 230" aria-hidden="true">
    <path d="M0 40 C140 8 300 40 420 118 L420 150 C300 82 150 62 0 82 Z" fill="var(--green)"/>
    <path d="M0 92 C150 72 300 100 420 166 L420 230 L0 230 Z" fill="var(--charcoal)"/>
  </svg>
  <div class="band-text slogan">SIMPLY I DO.<br>FAR AND ABOVE.</div>
</section>

<section class="card card--back">
  <div class="brand">
    <span class="brand__mark"></span>
    <div>
      <div class="brand__name">DANIEL MORVIK</div>
      <div class="brand__tagline">REAL ESTATE AGENT</div>
    </div>
  </div>

  <div class="headshot" role="img" aria-label="Headshot photo of the agent"></div>

  <div class="office">
    <span class="office__mark"></span>
    <span class="office__name">BRAMWELL PEAK REALTY</span>
  </div>
  <p class="address">2271 Lindqvist St.<br>Vancouver, BC<br>V5K 2P8</p>

  <ul class="contacts">
    <li>
      <svg viewBox="0 0 20 20"><rect width="20" height="20" rx="3" fill="var(--green)"/><path d="M6 4.5h2.5l1 3-1.5 1a7 7 0 0 0 3.5 3.5l1-1.5 3 1V14a1.5 1.5 0 0 1-1.5 1.5A9.5 9.5 0 0 1 4.5 6 1.5 1.5 0 0 1 6 4.5z" fill="var(--white)"/></svg>
      <span class="contacts__label">CELL</span>604-555-0148
    </li>
    <li>
      <svg viewBox="0 0 20 20"><rect width="20" height="20" rx="3" fill="var(--green)"/><path d="M6 4.5h2.5l1 3-1.5 1a7 7 0 0 0 3.5 3.5l1-1.5 3 1V14a1.5 1.5 0 0 1-1.5 1.5A9.5 9.5 0 0 1 4.5 6 1.5 1.5 0 0 1 6 4.5z" fill="var(--white)"/></svg>
      <span class="contacts__label">OFFICE</span>604-555-0192
    </li>
    <li>
      <svg viewBox="0 0 20 20"><rect width="20" height="20" rx="3" fill="var(--green)"/><rect x="6" y="4" width="8" height="4" fill="var(--white)"/><rect x="4" y="8.5" width="12" height="5" fill="var(--white)"/><rect x="6" y="14" width="8" height="2.5" fill="var(--white)"/></svg>
      <span class="contacts__label">FAX</span>604-555-0193
    </li>
  </ul>

  <svg class="swoosh" viewBox="0 0 420 230" aria-hidden="true">
    <path d="M0 40 C140 8 300 40 420 118 L420 150 C300 82 150 62 0 82 Z" fill="var(--green)"/>
    <path d="M0 92 C150 72 300 100 420 166 L420 230 L0 230 Z" fill="var(--charcoal)"/>
  </svg>
  <div class="band-text website">www.danielmorvik.example</div>
</section>

</body>
</html>
```